Wedding Dried Apple Label / Name Place Card

We are looking for a simple but stylish label to be attached via string to a bag of dried apples from my family's fruit farm. The size of the label we think should be similar to the size of a business card. The packaging will be a plastic bag: 4" x 2" x 6".
We would like it to say something like:
Remy & Joss
Est. Sept 10, 2017
Dried Apple Slices
Product of Quenton Fruit Farm
________________
(We need a spot to write in the name of the person and a table number)
Our colors are also grey and navy, and would like these colors to be used.
We have uploaded a photo of the plastic bag.
Wedding

```html
<!DOCTYPE html>
<html lang="en">
<head>
<meta charset="utf-8">
<title>Remy &amp; Joss – Dried Apple Slices Tag</title>
<link rel="stylesheet" href="https://fonts.googleapis.com/css2?family=Great+Vibes&family=Cinzel:wght@400&family=Kaushan+Script&family=Archivo+Narrow:ital,wght@1,400&family=Arimo&display=swap">
<style>
  :root {
    --navy: #13446a;
    --white: #ffffff;
    --mist: #bccad6;
    --label-grey: #c6c6c6;
    --ink: #111111;
    --flower-light: #dfe8f0;
    --flower-mid: #8aa4bd;
  }
  html, body { margin: 0; padding: 0; overflow: hidden; background: var(--white); }
  .canvas { width: 1200px; height: 1200px; position: relative; }
  .canvas svg { display: block; width: 1200px; height: 1200px; }
  .tag-body { fill: var(--navy); }
  .stitch { fill: none; stroke: var(--white); stroke-width: 1.6; stroke-dasharray: 6 4; }
  .hang-hole { fill: var(--white); }
  .couple-name { font-family: "Great Vibes", cursive; font-size: 46px; fill: var(--white); }
  .est-line { font-family: "Arimo", Arial, sans-serif; font-size: 15px; fill: var(--mist); }
  .product-title { font-family: "Cinzel", serif; font-size: 40px; fill: var(--white); }
  .farm-line { font-family: "Arimo", Arial, sans-serif; font-size: 17px; fill: var(--white); }
  .field-label { font-family: "Kaushan Script", cursive; font-size: 36px; fill: var(--mist); }
  .name-box { fill: var(--mist); }
  .guest-name { font-family: "Great Vibes", cursive; font-size: 48px; fill: var(--ink); }
  .table-digit { font-family: "Kaushan Script", cursive; font-size: 56px; fill: var(--white); }
  .side-caption { font-family: "Archivo Narrow", sans-serif; font-style: italic; font-size: 62px; fill: var(--label-grey); }
  .art-line { fill: var(--mist); opacity: .35; }
</style>
</head>
<body>
<main class="canvas">
  <svg viewBox="0 0 1500 1500" xmlns="http://www.w3.org/2000/svg">
    <defs>
      <path id="apple-shape" d="M50,140 C130,95 230,95 300,190 L298,108 L385,118 L345,200 L330,255 C380,240 440,240 500,265 L462,218 L598,213 L590,255 C660,225 740,240 822,282 L720,345 C770,390 780,470 765,540 C745,640 660,720 545,775 C500,780 470,760 420,715 C380,745 320,750 270,740 C170,700 90,600 70,470 C60,380 80,300 140,255 L175,240 Z"/>
      <linearGradient id="flower-tone" x1="0" y1="0" x2="1" y2="1">
        <stop offset="0" stop-color="var(--flower-light)"/>
        <stop offset="1" stop-color="var(--flower-mid)"/>
      </linearGradient>
    </defs>

    <!-- Front of tag -->
    <g class="tag tag-front">
      <use href="#apple-shape" class="tag-body"/>
      <use href="#apple-shape" class="stitch" transform="translate(430 440) scale(.93) translate(-430 -440)"/>
      <circle class="hang-hole" cx="430" cy="280" r="18"/>

      <text class="couple-name" x="308" y="330" text-anchor="middle">Remy &amp; Joss</text>
      <text class="est-line" x="312" y="360" text-anchor="middle">Est. Sept 10, 2016</text>
      <text class="product-title" x="318" y="428" text-anchor="middle">DRIED</text>
      <text class="product-title" x="318" y="472" text-anchor="middle">APPLE SLICES</text>
      <text class="farm-line" x="313" y="502" text-anchor="middle">Product of Quenton Fruit Farm</text>

      <g role="img" aria-label="Line illustration of two doves on a leafy branch with a nest">
        <rect class="art-line" x="228" y="522" width="196" height="136" rx="40"/>
      </g>
      <g role="img" aria-label="Illustration of pale blue roses tied with a curling ribbon">
        <path d="M600,310 C680,300 700,380 690,420 C720,500 720,620 690,680 C650,730 590,730 540,690 C480,660 460,620 480,590 C500,540 510,480 520,440 C540,400 570,380 600,360 Z" fill="url(#flower-tone)" opacity=".9"/>
      </g>
    </g>

    <!-- Back of tag -->
    <g class="tag tag-back">
      <use href="#apple-shape" class="tag-body" transform="translate(1455 560) scale(-1 1)"/>
      <use href="#apple-shape" class="stitch" transform="translate(1455 560) scale(-1 1) translate(430 440) scale(.93) translate(-430 -440)"/>
      <circle class="hang-hole" cx="1032" cy="828" r="18"/>

      <text class="field-label" x="1026" y="890" text-anchor="middle">surname</text>
      <rect class="name-box" x="818" y="912" width="399" height="81" rx="5"/>
      <text class="guest-name" x="1012" y="970" text-anchor="middle">Ms. Whitaker</text>
      <text class="field-label" x="1022" y="1040" text-anchor="middle">table number</text>
      <text class="table-digit" x="1025" y="1105" text-anchor="middle">5</text>

      <g role="img" aria-label="Line illustration of two wine glasses framed by grapevines">
        <rect class="art-line" x="896" y="1085" width="232" height="140" rx="40"/>
      </g>
    </g>

    <text class="side-caption" x="160" y="892">front</text>
    <text class="side-caption" x="990" y="1400">back</text>
  </svg>
</main>
</body>
</html>
```